Business card design needed

am looking for a fun and funky design to match our moto, seriously fun swimwear and fashion for girls.

We manufacture and retail girls swimwear and fashion in Australia. Our designs are fun loving and funky. I would like to use bright fuschia to match our website www.breezyplum.com.au. We target a higher end market so need it to reflect this.

Industry/Entity Type

Fashion

Contact Information for Business Card

Breezy Plum logo,
Maddie Lorne
(07) 35517204
admin@breezyplum.com.au
www.breezyplum.com.au

Logo Text

Breezy Plum

```html
<!DOCTYPE html>
<html lang="en">
<head>
<meta charset="utf-8">
<title>Breezy Plum — Business Card</title>
<link rel="stylesheet" href="https://fonts.googleapis.com/css2?family=Oswald:wght@400;500&display=swap">
<style>
  :root {
    --page-bg: #ece8e4;
    --fuchsia: #c8126e;
    --fuchsia-light: #d8247f;
    --fuchsia-deep: #a50d5a;
    --ink-black: #050505;
    --ink-charcoal: #2a2a2a;
    --white: #ffffff;
    --candy-pink: #e8a6c6;
    --rule: rgba(255,255,255,0.55);
  }
  * { box-sizing: border-box; margin: 0; padding: 0; }
  html, body {
    width: 1200px; height: 1024px; overflow: hidden;
    background: var(--page-bg);
    font-family: "Oswald", "Arial Narrow", sans-serif;
  }
  .sheet {
    width: 1200px; height: 1024px;
    display: flex; flex-direction: column; align-items: center;
    justify-content: center; gap: 40px;
  }
  .card {
    position: relative; width: 820px; height: 469px;
    border-radius: 4px; overflow: hidden;
    box-shadow: 0 10px 28px rgba(0,0,0,0.18);
  }
  /* Front */
  .card--front {
    background: linear-gradient(135deg, var(--fuchsia-light) 0%, var(--fuchsia) 50%, var(--fuchsia-deep) 100%);
    color: var(--white);
  }
  .card__divider {
    position: absolute; top: 0; bottom: 0; left: 500px;
    width: 1px; background: var(--rule);
  }
  .brand {
    position: absolute; display: flex; align-items: center;
    color: var(--white); font-weight: 400; white-space: nowrap;
  }
  .brand__dot {
    border-radius: 50%; background: var(--candy-pink);
    border: 3px solid var(--white); flex: none;
  }
  .card--front .brand { left: 48px; bottom: 150px; font-size: 44px; gap: 16px; }
  .card--front .brand__dot { width: 46px; height: 46px; }
  .contact {
    position: absolute; left: 540px; top: 90px;
  }
  .contact__name {
    font-size: 38px; font-weight: 500; letter-spacing: 0.5px;
    padding-bottom: 14px; margin-bottom: 22px;
    border-bottom: 1px solid var(--rule);
    width: 250px;
  }
  .contact__list { list-style: none; }
  .contact__item {
    display: flex; align-items: center; gap: 12px;
    font-size: 17px; font-weight: 400; margin-bottom: 14px;
  }
  .contact__icon { width: 18px; height: 18px; flex: none; }
  /* Back */
  .card--back {
    background: radial-gradient(ellipse at 50% 45%, var(--ink-charcoal) 0%, var(--ink-black) 75%);
    display: flex; align-items: center; justify-content: center;
  }
  .card--back .brand {
    position: static; font-size: 84px; gap: 26px;
  }
  .card--back .brand__dot { width: 80px; height: 80px; border-width: 5px; }
</style>
</head>
<body>
<main class="sheet">
  <section class="card card--front" aria-label="Card front">
    <div class="card__divider"></div>
    <div class="brand">
      <span class="brand__dot"></span>
      <span class="brand__name">Breezy Plum</span>
    </div>
    <div class="contact">
      <h1 class="contact__name">Maddie Lorne</h1>
      <ul class="contact__list">
        <li class="contact__item">
          <svg class="contact__icon" viewBox="0 0 24 24" aria-hidden="true"><path fill="#fff" d="M6.6 10.8a15 15 0 0 0 6.6 6.6l2.2-2.2c.3-.3.7-.4 1-.2 1.1.4 2.3.6 3.6.6.6 0 1 .4 1 1V20c0 .6-.4 1-1 1A17 17 0 0 1 3 4c0-.6.4-1 1-1h3.5c.6 0 1 .4 1 1 0 1.3.2 2.5.6 3.6.1.3 0 .7-.2 1z"/></svg>
          <span>(07) 35517204</span>
        </li>
        <li class="contact__item">
          <svg class="contact__icon" viewBox="0 0 24 24" aria-hidden="true"><rect x="2" y="5" width="20" height="14" rx="2" fill="#fff"/><path d="M3 6l9 7 9-7" fill="none" stroke="#c8126e" stroke-width="2"/></svg>
          <span>admin@breezyplum.com.au</span>
        </li>
        <li class="contact__item">
          <svg class="contact__icon" viewBox="0 0 24 24" aria-hidden="true"><circle cx="12" cy="12" r="10" fill="#fff"/><g fill="none" stroke="#c8126e" stroke-width="1.5"><ellipse cx="12" cy="12" rx="4" ry="9.5"/><path d="M2.5 12h19M4 7h16M4 17h16"/></g></svg>
          <span>www.breezyplum.com.au</span>
        </li>
      </ul>
    </div>
  </section>

  <section class="card card--back" aria-label="Card back">
    <div class="brand">
      <span class="brand__dot"></span>
      <span class="brand__name">Breezy Plum</span>
    </div>
  </section>
</main>
</body>
</html>
```